Mirela Causo Photography

I need a website design for my photography business, I want something clean, elegant, Classy.. I like the colors, White, Black, Green/Blue, Pink, Brown, Lavender,, I have a lot added my Logo .... Additional Info... I need a Photography Website Design, with probably 6 Tabs, Home, About Me, Portfolio, Gallery, Investment, Contact.
Home Page should have my logo, Name & Address, Social Media Icons, and Pictures.
As long as the templates are made I have a hosting coming that will code it.
Target Market(s)
Portraits Photography, Senior Portraits, Newborn, Families, Events, Engagements, Wedding,
Industry/Entity Type
Business
Number of Pages Required
5+ page
Look and feel

```html
<!DOCTYPE html>
<html lang="en">
<head>
<meta charset="utf-8">
<title>Mirela Causo Photography</title>
<link rel="stylesheet" href="https://fonts.googleapis.com/css2?family=Questrial&display=swap">
<style>
:root{
  --teal:#17a38c;
  --teal-dark:#0f8a76;
  --ink:#3b3b3d;
  --grey:#9a9a9c;
  --light:#d9dcdc;
  --white:#ffffff;
  --footer:#404042;
}
*{margin:0;padding:0;box-sizing:border-box}
html,body{width:1200px;height:2933px;overflow:hidden;background:var(--white)}
body{font-family:"Questrial",sans-serif;color:var(--ink);position:relative}
.abs{position:absolute}

/* header */
.site-header{position:absolute;left:0;top:0;width:1200px;height:188px;background:var(--white)}
.brand{position:absolute;left:0;width:1200px;top:14px;text-align:center}
.brand-mark{display:block;margin:0 auto 10px;width:64px;height:64px;border-radius:50%;background:var(--ink)}
.brand-name{font-size:40px;color:var(--ink);letter-spacing:2px;line-height:1}
.nav a{position:absolute;top:144px;font-size:14px;color:var(--grey);text-decoration:none;letter-spacing:1px}
.nav a.active{color:var(--teal)}
.social-top{position:absolute;top:14px;left:898px;display:flex;gap:14px}
.social-top span{width:16px;height:16px;border-radius:50%;background:var(--teal);opacity:.75}
.phone-top{position:absolute;top:58px;left:896px;font-size:18px;color:var(--grey);display:flex;align-items:center;gap:8px}

/* hero */
.hero{position:absolute;left:0;top:188px;width:1200px;height:619px;
  background:radial-gradient(ellipse at 50% 40%,#2a2624 0%,#4a3d33 35%,#7a6652 60%,#3a302a 100%)}
.hero-title{position:absolute;left:0;width:1200px;top:292px;text-align:center;font-size:78px;color:var(--white);letter-spacing:3px}
.hero-sub{position:absolute;left:0;width:1200px;top:382px;text-align:center;font-size:24px;color:var(--white);letter-spacing:1px}

/* section titles */
.section-title{position:absolute;left:0;width:1200px;text-align:center;font-size:29px;color:var(--teal);letter-spacing:1px}

.about-text{position:absolute;left:226px;width:748px;top:918px;text-align:center;font-size:18px;line-height:23px;color:var(--grey)}
.about-text b{font-weight:normal;color:var(--ink)}
.about-rule{position:absolute;left:506px;top:1003px;width:174px;height:2px;background:var(--grey)}

/* portfolio */
.portfolio-panel{position:absolute;top:1139px;height:379px}
.panel-left{left:0;width:403px;background:linear-gradient(135deg,#1aa88f,#128a76 60%,#16a08a)}
.panel-mid{left:403px;width:394px;background:linear-gradient(180deg,#c9b9a8 0%,#7f6f68 35%,#3e3a44 70%,#2a2a33 100%)}
.panel-right{left:797px;width:403px;background:linear-gradient(180deg,#1ba38c,#17a08a 55%,#129079)}
.panel-caption{position:absolute;left:427px;width:346px;top:1333px;text-align:center;font-size:14px;line-height:17px;color:var(--white)}
.read-more{position:absolute;left:403px;width:394px;top:1489px;text-align:center;font-size:14px;color:var(--white)}

/* gallery */
.gallery-item{position:absolute;border:4px solid var(--teal)}
.view-gallery{position:absolute;left:870px;top:2100px;width:159px;height:39px;border:2px solid var(--teal);color:var(--teal);font-size:16px;letter-spacing:1px;display:flex;align-items:center;justify-content:center}

/* contact */
.field{position:absolute;border:1px solid var(--light);font-size:14px;color:var(--teal);letter-spacing:1px;padding:10px 9px}
.send{position:absolute;left:296px;top:2574px;width:633px;height:36px;background:var(--teal);color:var(--white);font-size:15px;letter-spacing:2px;display:flex;align-items:center;justify-content:center}

/* footer */
.site-footer{position:absolute;left:0;top:2679px;width:1200px;height:254px;background:var(--footer);color:var(--white)}
.footer-line{position:absolute;left:0;width:1200px;display:flex;justify-content:center;align-items:center;gap:8px}
.footer-social span{position:absolute;top:147px;width:38px;height:38px;border-radius:50%;background:var(--teal)}
.copyright{position:absolute;left:0;width:1200px;top:214px;text-align:center;font-size:14px;color:#d0d0d0}
.footer-brand{position:absolute;left:855px;top:168px;font-size:28px;color:#6a6a6c}
</style>
</head>
<body>

<header class="site-header">
  <div class="brand">
    <span class="brand-mark"></span>
    <div class="brand-name">Mirela Causo Photography</div>
  </div>
  <nav class="nav">
    <a class="active" style="left:176px">HOME</a>
    <a style="left:258px">ABOUT ME</a>
    <a style="left:370px">PORTFOLIO</a>
    <a style="left:772px">GALLERY</a>
    <a style="left:872px">INVESTMENT</a>
    <a style="left:985px">CONTACT</a>
  </nav>
  <div class="social-top"><span></span><span></span><span></span><span></span><span></span></div>
  <div class="phone-top">
    <svg width="12" height="22" viewBox="0 0 12 22"><rect x="1" y="1" width="10" height="20" rx="2" fill="none" stroke="#17a38c" stroke-width="2"/><circle cx="6" cy="17" r="1.3" fill="#17a38c"/></svg>
    0100-555-782
  </div>
</header>

<section class="hero" role="img" aria-label="Photograph of a person in a knit sweater holding a film camera at chest height"></section>
<div class="hero-title">Mirela Causo</div>
<div class="hero-sub">PROFESSIONAL PHOTOGRAPHER</div>

<h2 class="section-title" style="top:852px">ABOUT ME</h2>
<p class="about-text">Lorem ipsum dolor sit amet, <b>consectetuer adipiscing</b> elit, sed diam nonummy nibh euismod tincidunt ut laoreet dolore magna aliquam erat volutpat. Ut wisi enim ad minim veniam, <b>quis nostrud exerci</b> tation ullamcorper suscipit lobortis nisl ut aliquip ex ea commodo consequat.</p>
<div class="about-rule"></div>

<h2 class="section-title" style="top:1070px">PORTFOLIO</h2>
<div class="portfolio-panel panel-left" role="img" aria-label="Close-up photograph of a camera lens with a teal overlay"></div>
<div class="portfolio-panel panel-mid" role="img" aria-label="Photograph of a woman seen from behind looking over a hazy city at dusk"></div>
<div class="portfolio-panel panel-right" role="img" aria-label="Photograph of a man standing on a shore with mountains behind, teal overlay"></div>
<p class="panel-caption">Lorem ipsum dolor sit amet, consectetuer adipiscing elit, sed diam nonummy nibh euismod tincidunt ut laoreet dolore magna aliquam erat volutpat.</p>
<div class="read-more">Read more</div>

<h2 class="section-title" style="top:1578px">GALLERY</h2>
<div class="gallery-item" style="left:171px;top:1660px;width:301px;height:185px;background:linear-gradient(180deg,#6f7580,#45484f 50%,#5a4a44)" role="img" aria-label="Photograph of a busy city street in traffic"></div>
<div class="gallery-item" style="left:171px;top:1860px;width:301px;height:186px;background:linear-gradient(180deg,#2c3035,#4a4f4f 60%,#6b6f6a)" role="img" aria-label="Photograph of a hooded figure among white flowers"></div>
<div class="gallery-item" style="left:481px;top:1660px;width:294px;height:229px;background:linear-gradient(180deg,#8fb2c9,#a07a6a 60%,#6a4a3e)" role="img" aria-label="Photograph of a suspension bridge walkway"></div>
<div class="gallery-item" style="left:481px;top:1901px;width:294px;height:235px;background:linear-gradient(180deg,#b8cfd8,#e3dccb 45%,#d9b49a)" role="img" aria-label="Photograph of people relaxing on a sandy beach"></div>
<div class="gallery-item" style="left:782px;top:1660px;width:245px;height:395px;background:linear-gradient(180deg,#1a1a1a,#3c3c3c 50%,#202020)" role="img" aria-label="Black and white photograph of musicians performing on stage"></div>
<div class="view-gallery">VIEW GALLERY</div>

<h2 class="section-title" style="top:2240px">CONTACT&nbsp; US</h2>
<form>
  <div class="field" style="left:296px;top:2310px;width:313px;height:39px">NAME</div>
  <div class="field" style="left:616px;top:2310px;width:313px;height:39px">LAST NAME</div>
  <div class="field" style="left:296px;top:2354px;width:313px;height:39px">EMAIL</div>
  <div class="field" style="left:616px;top:2354px;width:313px;height:39px">PHONE</div>
  <div class="field" style="left:296px;top:2400px;width:633px;height:169px">MESSAGE</div>
  <div class="send">SEND</div>
</form>

<footer class="site-footer">
  <div class="footer-line" style="top:52px;font-size:16px">
    <svg width="16" height="22" viewBox="0 0 16 22"><path d="M8 1a7 7 0 0 0-7 7c0 5 7 13 7 13s7-8 7-13a7 7 0 0 0-7-7z" fill="#fff"/><circle cx="8" cy="8" r="2.6" fill="#404042"/></svg>
    2140 Linden Avenue&nbsp; Maplewood, NY 10420
  </div>
  <div class="footer-line" style="top:94px;font-size:20px">
    <svg width="13" height="22" viewBox="0 0 12 22"><rect x="1" y="1" width="10" height="20" rx="2" fill="#17a38c"/><circle cx="6" cy="17" r="1.3" fill="#fff"/></svg>
    0100-555-782
  </div>
  <div class="footer-social">
    <span style="left:445px"></span><span style="left:516px"></span><span style="left:590px"></span><span style="left:663px"></span><span style="left:736px"></span>
  </div>
  <div class="copyright">©2015 copyright. mirelacausophotography.com</div>
  <div class="footer-brand">Mirela Causo</div>
</footer>

</body>
</html>
```